Billboard for personal injury chiropractors office

We are a personal injury chiropractor clinic.
I need a Billboard with the company name as the dominating factor. Also a smaller picture or 2 of something creative, like a car accident or an arm in a cast off to the sides.
We Like something Clean and Simple and Eye Catching. Please make the picture Small and Off To The Side. The MAIN FOCUS areas are the… name Varden Chiropractic Clinic
At the top CAR ACCIDENT INJURY?
AND at the bottom our number 418-27-FLEXA.
Dr.Milo R. Varden in bold somewhere with the word chiropractor under the doctors name in a text.

Im open to red lettering on white backgrounds, red on yellow backgrounds and I'm also open to reds blues white and yellow. I'd prefer yellow if used be across the bottom.

I am uploading a very rough draft of what we are after along with a screenshot of the tv commercial showing the yellow

DO NOT USE THE LOGO ON THE COMMERCIAL. I JUST WANT THE NAME TYPED LIKE ON SAMPLE BILLBOARD.

Industry/Entity Type

Chiropractic

Colors
0054AA
0677BA
7BADD7
CADEEF
E8F1F8
FFF300
FFF600
FEFA6F
FFFEC7
FFFEE8
EB3D1F
EC4F4E
F09395
F8D3D4
FCEDEE

Requirements
Must have
• Eye catching ,bold

```html
<!DOCTYPE html>
<html lang="en">
<head>
<meta charset="utf-8">
<title>Varden Chiropractic Clinic – Billboard</title>
<link rel="stylesheet" href="https://fonts.googleapis.com/css2?family=Archivo+Black&family=Tinos:wght@700&display=swap">
<style>
  :root {
    --blue: #0054AA;
    --blue-mid: #0677BA;
    --blue-light: #7BADD7;
    --blue-pale: #CADEEF;
    --red: #E41E26;
    --yellow: #FFF300;
    --yellow-soft: #FEFA6F;
    --yellow-pale: #FFFEC7;
    --page: #ECEEF1;
  }
  html, body {
    margin: 0;
    width: 1200px;
    height: 962px;
    overflow: hidden;
    background: var(--page);
  }
  body {
    display: flex;
    align-items: center;
    justify-content: center;
  }
  .billboard {
    width: 1160px;
    height: auto;
    display: block;
    box-shadow: 0 4px 18px rgba(0,0,0,0.15);
  }
  .clinic-name { font-family: "Archivo Black", "Arial Black", sans-serif; fill: var(--blue); }
  .headline-top { font-family: "Archivo Black", "Arial Black", sans-serif; fill: var(--blue); }
  .headline-main { font-family: "Archivo Black", "Arial Black", sans-serif; fill: var(--red); }
  .phone { font-family: "Archivo Black", "Arial Black", sans-serif; fill: var(--blue); }
  .doctor { font-family: "Tinos", "Times New Roman", serif; font-weight: 700; fill: var(--blue); }
  .doctor-title { font-family: "Tinos", "Times New Roman", serif; font-weight: 700; fill: var(--red); }
</style>
</head>
<body>
<svg class="billboard" viewBox="0 0 1860 473" xmlns="http://www.w3.org/2000/svg" aria-label="Varden Chiropractic Clinic billboard">
  <defs>
    <linearGradient id="top-band" x1="0" y1="0" x2="1" y2="0">
      <stop offset="0.08" stop-color="#FFF300"/>
      <stop offset="0.35" stop-color="#FEFA6F"/>
      <stop offset="0.62" stop-color="#FFFEE8"/>
      <stop offset="0.8" stop-color="#FFFFFF" stop-opacity="0"/>
    </linearGradient>
    <linearGradient id="panel-bg" x1="0" y1="0" x2="1" y2="0">
      <stop offset="0.45" stop-color="#FFFFFF"/>
      <stop offset="0.85" stop-color="#EDEAE6"/>
    </linearGradient>
    <linearGradient id="photo-fill" x1="0" y1="0" x2="1" y2="0">
      <stop offset="0" stop-color="#EDEAE6" stop-opacity="0"/>
      <stop offset="0.25" stop-color="#E0303A"/>
      <stop offset="0.7" stop-color="#C81A28"/>
      <stop offset="1" stop-color="#D9D9D9"/>
    </linearGradient>
  </defs>

  <rect class="panel" x="0" y="0" width="1860" height="473" fill="url(#panel-bg)"/>

  <rect x="0" y="0" width="1860" height="40" fill="url(#top-band)"/>
  <polygon points="0,0 70,0 40,40 0,40" fill="var(--yellow-pale)"/>
  <polygon points="70,0 110,0 80,40 40,40" fill="var(--yellow-soft)"/>

  <rect x="1500" y="0" width="360" height="433" fill="url(#photo-fill)" role="img" aria-label="Photo of a red car with a crumpled front and broken headlight"/>

  <polygon points="0,363 678,363 798,473 0,473" fill="var(--yellow)"/>
  <polygon points="678,363 730,363 850,473 798,473" fill="var(--yellow-soft)"/>
  <polygon points="730,363 790,363 910,473 850,473" fill="var(--yellow-pale)"/>

  <polygon points="968,433 1010,433 990,473 928,473" fill="var(--blue-pale)"/>
  <polygon points="1010,433 1040,433 1020,473 990,473" fill="var(--blue-light)"/>
  <polygon points="1040,433 1080,433 1060,473 1020,473" fill="var(--blue-mid)"/>
  <polygon points="1080,433 1860,433 1860,473 1060,473" fill="var(--blue)"/>

  <g class="clinic-name" aria-label="Varden Chiropractic Clinic">
    <text x="60" y="205" font-size="180" textLength="650" lengthAdjust="spacingAndGlyphs">VARDEN</text>
    <text x="62" y="300" font-size="68" textLength="646" lengthAdjust="spacingAndGlyphs">CHIROPRACTIC CLINIC</text>
  </g>

  <text class="phone" x="63" y="453" font-size="92" textLength="638" lengthAdjust="spacingAndGlyphs">418-27-FLEXA</text>

  <text class="headline-top" x="833" y="133" font-size="88" textLength="653" lengthAdjust="spacingAndGlyphs">CAR ACCIDENT</text>
  <text class="headline-main" x="836" y="278" font-size="166" textLength="660" lengthAdjust="spacingAndGlyphs">INJURY?</text>

  <text class="doctor" x="840" y="350" font-size="60" textLength="644" lengthAdjust="spacingAndGlyphs">DR.MILO R. VARDEN</text>
  <text class="doctor-title" x="840" y="396" font-size="48" textLength="441" lengthAdjust="spacingAndGlyphs">CHIROPRACTOR</text>
</svg>
</body>
</html>
```